14 years in business and its time for a new look and feel brochure and business cards!

We are looking to create a brochure that is professional and eye catching to bring in new commercial business. After14 years in business we have finally redone our logo and it is time to get a brochure completed as well. The logo that should be used is the one that says Inc. We want this new brochure to appeal to corporate property management companies and smaller apartment complexes. We want it to look rich and have the same high quality our work has.

Target Market(s)

property management companies and apartment complexes in the DMV.

Industry/Entity Type

Construction Company

Contact Information for Business Card

Logo
Dovid Markel
CEO
Mobile 410-555-0187
Office 410-555-0142
Address 3417 Harlow Lane Suite C Baltimore, MD 21290
Email DM@BrightCoatProsInc.example

Font styles to use
Sans Serif

Requirements
Must have
• Want the background to be black and silver gradient. Will be printing on high gloss and would like for it to be rich looking.
• brochure will be 8.5x11. open minded in terms of the fold, how it looks best with the design provided will determine that. Can be bi-fold, try-fold or z-fold.
• Content for brochure:About us
• Founded in 2003, BrightCoat Pros Inc. was the vision of Dovid Markel, with a commitment to becoming the premier renovator and developer of residential and commercial properties in the DMV. Today, BrightCoat Pros Inc. is widely respected for their gold standard in quality and efficiency and continues to grow by attracting the highest level of professionals with knowledge and experience in our field.
• BrightCoat Pros Inc.’s most valuable asset is our team members. The efforts they put forth are the key to meeting our standards and providing all of our valued clients with the highest quality of service. Leading our wonderful team members is a group of management like no other. With years of experience, the power to motivate and the keen eye to ensure top quality, our team of experts focus all of their energy to exceed our client’s expectations.
• Our Mission
• We strive to provide timely delivery, the highest level of quality and value on every project. We offer unsurpassed dedication to maintain our working relationships and consistently deliver the best service to ensure our clients success.
• Property Renovations
• BrightCoat Pros Inc. has been responsible for coordinating the construction and renovation of many projects, including all parts of a building’s interior and exterior. Well known for attention to details, quality and timely execution, BrightCoat Pros Inc. has managed and executed more than 4,000 turnovers and over 150 projects in the last 3 years alone.
• Renovations not only improve the appeal and marketability of your property, but also add value. Interior and exterior renovations help make any property more functional, energy-efficient and enable you to keep up with what your market demands. From the smallest change of a door knob to a complete kitchen overhaul, these are the things that make all the difference in your property. We are committed to deliver great value, and we do that by ensuring that our experts are involved in the renovation process, providing input and quality maintenance throughout the entire renovation.
• Services Include
• Painting
• Flooring
• Sub-Flooring
• Crown molding
• Siding & Wood Replacement
• Trim & Carpentry Work
• Punches
• Decks
• Power wash
• Concrete & Paving
• Turnovers including plumbing and electric
• Kitchen overhauls
• We offer first time clients a free apartment paint or punch on us to show you the quality you can always expect!
• Call today to schedule your first-time paint or punch at 410-555-0142.

```html
<!DOCTYPE html>
<html lang="en">
<head>
<meta charset="utf-8">
<title>BrightCoat Pros Inc. – Brochure Covers</title>
<link rel="stylesheet" href="https://fonts.googleapis.com/css2?family=Lato:wght@400;700&family=Michroma&display=swap">
<style>
  :root {
    --bg: #e9ecef;
    --slate: #5c5d66;
    --slate-dark: #4d4e57;
    --slate-faint: #6c6d77;
    --silver-light: #f4f4f6;
    --silver: #d9d9de;
    --silver-mid: #b9bac1;
    --ink: #55565e;
    --paper: #ffffff;
  }
  * { box-sizing: border-box; margin: 0; padding: 0; }
  html, body { width: 1200px; height: 789px; overflow: hidden; background: var(--bg); }
  .spread {
    position: absolute; left: 59px; top: 44px;
    width: 1082px; height: 701px;
    display: flex;
    box-shadow: 0 10px 30px rgba(0,0,0,.18);
  }
  .panel { position: relative; width: 541px; height: 701px; overflow: hidden; }

  /* Back cover */
  .back-cover { background: linear-gradient(160deg, var(--slate) 0%, var(--slate-dark) 100%); color: var(--silver); }
  .back-mark {
    position: absolute; left: 90px; top: 110px; width: 360px; height: 360px;
    display: flex; align-items: center; justify-content: center; gap: 14px;
  }
  .back-mark .ring { width: 300px; height: 300px; border-radius: 50%; border: 26px solid var(--slate-faint); position: absolute; }
  .back-mark .name { font-family: "Michroma", sans-serif; font-size: 26px; color: var(--slate-faint); position: relative; text-align: center; line-height: 1.3; }
  .offer {
    position: absolute; left: 40px; right: 40px; top: 520px;
    font-family: "Lato", sans-serif; font-weight: 700; font-size: 15px; line-height: 1.35; text-align: center;
  }
  .offer-phone {
    position: absolute; left: 0; right: 0; top: 600px; text-align: center;
    font-family: "Michroma", sans-serif; font-size: 44px; color: var(--silver-light); letter-spacing: 1px;
  }

  /* Front cover */
  .front-cover { background: linear-gradient(180deg, var(--silver-light), var(--silver)); }
  .front-cover svg.bands { position: absolute; inset: 0; }
  .brand {
    position: absolute; left: 0; right: 0; top: 78px;
    display: flex; align-items: center; justify-content: center; gap: 10px;
  }
  .brand .dot { width: 22px; height: 22px; border-radius: 50%; background: var(--ink); }
  .brand .name { font-family: "Michroma", sans-serif; font-size: 19px; color: var(--ink); }
  .hero-photo {
    position: absolute; left: 0; right: 0; top: 168px; height: 360px;
    background: linear-gradient(180deg, #cfd3d6 0%, #b9bcbd 28%, #8a6a5e 48%, #7a675c 62%, #5d7a3e 78%, #4f6d33 100%);
  }
  .title-box {
    position: absolute; left: 40px; right: 40px; top: 470px; height: 110px;
    background: linear-gradient(180deg, var(--paper), var(--silver-light));
    border: 3px solid var(--silver-mid); border-radius: 14px;
    display: flex; align-items: center; justify-content: center;
  }
  .title-box h1 { font-family: "Michroma", sans-serif; font-weight: 400; font-size: 31px; color: var(--ink); letter-spacing: 1px; }
  .call-line {
    position: absolute; left: 0; right: 0; top: 598px; text-align: center;
    font-family: "Michroma", sans-serif; font-size: 14px; color: var(--ink);
  }
</style>
</head>
<body>
  <main class="spread">
    <section class="panel back-cover">
      <div class="back-mark" aria-hidden="true">
        <div class="ring"></div>
        <div class="name">BrightCoat<br>Pros Inc.</div>
      </div>
      <p class="offer">We offer first time clients a free apartment paint or punch on us to show you the quality you can always expect!<br>Call today to schedule your first-time paint or punch at</p>
      <p class="offer-phone">410-555-0142</p>
    </section>

    <section class="panel front-cover">
      <svg class="bands" width="541" height="701" viewBox="0 0 541 701" aria-hidden="true">
        <path d="M0 0 H541 V30 Q270 70 0 40 Z" fill="#6a6b74"/>
        <path d="M0 40 Q270 70 541 30 V42 Q270 84 0 52 Z" fill="#9c9da5"/>
        <path d="M0 140 Q270 170 541 130 V168 H0 Z" fill="#8d8e96"/>
        <path d="M0 150 Q270 176 541 140 V168 H0 Z" fill="#6a6b74"/>
        <path d="M0 650 Q270 612 541 642 V701 H0 Z" fill="#7c7d86"/>
        <path d="M0 662 Q270 628 541 654 V701 H0 Z" fill="#5c5d66"/>
      </svg>
      <div class="brand">
        <span class="dot" aria-hidden="true"></span>
        <span class="name">BrightCoat Pros Inc.</span>
      </div>
      <div class="hero-photo" role="img" aria-label="Photo of a three-storey brick apartment complex with white balconies and a green lawn"></div>
      <div class="title-box"><h1>BRIGHTCOAT PROS</h1></div>
      <p class="call-line">Call Today At: 410-555-0142.</p>
    </section>
  </main>
</body>
</html>
```